Infographic to communicate Cyber Security and Insurance Product Offering for IT Service Providers

We need an inspirational infographic that shows how TrellaWorks works with QDR (an MSP partner) to help organisations close the loop on cyber risk. The design should illustrate the layers of the IT infrastructure stack and the systems and processes that wrap around it to protect and mitigate against risk.
At the core: MSP Services (Desktop, Software, Website). Surrounding this: TrellaWorks Governance & Protection, leading into an Incident layer that connects to TrellaWorks Insurance and Incident Response, linked by a continuous feedback loop. The outer circle should represent the constant threat of cyber attack.
TrellaWorks core offerings for this graphic:
Plinth Verify (compliance/assurance product)
Plinth Cover
QDR Primary Services (directly connected to TrellaWorks):
Managed IT Services
Disaster Recovery as a Service (DRaaS)
E8 Security Packages
Cloud Hosting & Infrastructure
QDR Secondary Services (supporting but not directly anchored):
Telephony & Unified Communications
Networking Services
Data Backup & Storage Solutions
Professional Services & Consulting
Procurement & Licensing
Training & User Awareness
Style: Modern, professional, and client-friendly, with a technology-inspired colour palette.
Deliverables: Polished colour version plus editable source files — preferably in Figma, or alternatively if not possible using either Adobe Illustrator (.AI) or a layered Photoshop (.PSD) (e.g. industry standards for editable design).
Rewards: The winning design prize will be increased by $100, and we will also award $50 each to the 2nd and 3rd place runner-ups, as our way of giving a little more back.
A simple wireframe visual guide has been uploaded as a reference, but this should in no way limit or restrict your creativity. We encourage original, innovative approaches to bring this concept to life.
Ownership & Exclusivity: As per ArtMarquee’s T&Cs, all rights to the winning design will transfer to us once the project is complete for our ongoing use. We also kindly ask that the work created here remain exclusive to this project, meaning it won’t be reused or lightly modified for other clients in the future. The reason is simple: once we’ve invested in and paid for a design, we want to be confident it won’t turn up on a competitor’s website with just a different colour scheme. Thanks again for respecting that. [Note:- The designs submitted so far haven’t quite hit the mark, so I’ve put together a couple of slides to clarify direction. These outline the key stakeholders, the current IT services and challenges, how the Morvane product addresses those challenges, and a simple version of what we’d like the infographic to convey. Please review these slides carefully, as they should give you a clearer understanding of the story we want the design to tell.]
Target Market(s)
Small to Medium sized businesses
Colors
Designer to choose colors to be used in the design.
Look and feel

```html
<!DOCTYPE html>
<html lang="en">
<head>
<meta charset="utf-8">
<title>Cyber Security and Insurance Product Offering for IT Service Providers</title>
<link href="https://fonts.googleapis.com/css2?family=Saira:wght@500;600;700&display=swap" rel="stylesheet">
<style>
  :root {
    --navy: #1f3a56;
    --ink: #0d0d0d;
    --icon: #4a6178;
    --ring-light: #cdd2d8;
    --ring-label-light: #b9c0c8;
    --core: #c5ced8;
    --paper: #ffffff;
  }
  html, body {
    margin: 0;
    padding: 0;
    width: 1200px;
    height: 1104px;
    overflow: hidden;
    background: var(--paper);
  }
  .infographic {
    display: block;
    width: 1200px;
    height: 1104px;
    font-family: "Saira", sans-serif;
  }
  .title { fill: var(--navy); font-weight: 600; font-size: 47px; text-anchor: middle; }
  .ring-dark { fill: none; stroke: var(--navy); stroke-width: 1.7; stroke-dasharray: 7 6; }
  .ring-light { fill: none; stroke: var(--ring-light); stroke-width: 1.7; stroke-dasharray: 7 6; }
  .ring-label { font-weight: 600; font-size: 17px; fill: var(--navy); }
  .ring-label--light { fill: var(--ring-label-light); }
  .outer-label { font-weight: 600; font-size: 17px; fill: var(--navy); }
  .inner-label { font-weight: 600; font-size: 17px; fill: var(--ink); }
  .icon-backing { fill: var(--paper); }
  .icon { fill: none; stroke: var(--icon); stroke-width: 2.4; stroke-linecap: round; stroke-linejoin: round; }
  .core-disc { fill: var(--core); }
  .core-title { fill: var(--ink); font-weight: 700; font-size: 48px; text-anchor: middle; }
  .mid { text-anchor: middle; }
  .end { text-anchor: end; }
</style>
</head>
<body>
<svg class="infographic" viewBox="0 0 1700 1564" xmlns="http://www.w3.org/2000/svg">
  <defs>
    <filter id="core-shadow" x="-20%" y="-20%" width="140%" height="140%">
      <feDropShadow dx="0" dy="3" stdDeviation="5" flood-color="#000" flood-opacity="0.18"/>
    </filter>
    <path id="arc-threat" d="M362,900 A483,483 0 0 1 1328,900"/>
    <path id="arc-incident" d="M427,900 A418,418 0 0 1 1263,900"/>
    <path id="arc-plinth" d="M503,900 A342,342 0 0 1 1187,900"/>
    <path id="arc-msp" d="M573,900 A272,272 0 0 1 1117,900"/>
  </defs>

  <!-- Heading -->
  <text class="title" x="848" y="165">Infographic for Cyber Security and</text>
  <text class="title" x="848" y="228">Insurance Product Offering for IT Service Providers</text>

  <!-- Rings -->
  <circle class="ring-dark" cx="845" cy="900" r="475"/>
  <circle class="ring-light" cx="845" cy="900" r="410"/>
  <circle class="ring-dark" cx="845" cy="900" r="335"/>
  <circle class="ring-light" cx="845" cy="900" r="265"/>

  <!-- Ring labels -->
  <text class="ring-label"><textPath href="#arc-threat" startOffset="24.6%">Constant Threat of Cyber Attack</textPath></text>
  <text class="ring-label ring-label--light"><textPath href="#arc-incident" startOffset="24%">Incident Response &amp; Insurance</textPath></text>
  <text class="ring-label mid"><textPath href="#arc-plinth" startOffset="50%">Plinth Verify &amp; Plinth Cover</textPath></text>
  <text class="ring-label ring-label--light"><textPath href="#arc-msp" startOffset="27%">MSP Services</textPath></text>

  <!-- Core -->
  <circle class="core-disc" cx="845" cy="900" r="125" filter="url(#core-shadow)"/>
  <text class="core-title" x="845" y="895">MSP</text>
  <text class="core-title" x="845" y="945">Services</text>

  <!-- Secondary services (outer ring) -->
  <g class="service service--training" transform="translate(833,428)">
    <rect class="icon-backing" x="-46" y="-34" width="92" height="68"/>
    <rect class="icon" x="-26" y="-22" width="52" height="36" rx="3"/>
    <path class="icon" d="M-5 14v8M5 14v8M-13 24h26"/>
    <path class="icon" d="M-5 -6v-4a5 5 0 0 1 10 0v4M-7 -6h14v11h-14z"/>
    <path class="icon" d="M-20 -12h7M13 -12h7M-20 4h7M13 4h7"/>
  </g>
  <text class="outer-label mid" x="848" y="379">Training &amp; User Awareness</text>

  <g class="service service--backup" transform="translate(1233,620)">
    <rect class="icon-backing" x="-38" y="-38" width="76" height="76"/>
    <rect class="icon" x="-26" y="-12" width="44" height="30" rx="3"/>
    <path class="icon" d="M-4 18v6M-12 26h16"/>
    <path class="icon" d="M-14 -4v-26h18l8 8v18"/>
    <path class="icon" d="M-9 -22h10M-9 -16h14M-9 -10h14"/>
    <circle class="icon" cx="18" cy="14" r="8"/>
    <circle class="icon" cx="18" cy="14" r="3"/>
  </g>
  <text class="outer-label" x="1285" y="606">Data Backup</text>
  <text class="outer-label" x="1285" y="631">&amp; Storage</text>

  <g class="service service--consulting" transform="translate(1305,1048)">
    <rect class="icon-backing" x="-38" y="-36" width="76" height="72"/>
    <rect class="icon" x="-20" y="-22" width="50" height="36" rx="2"/>
    <path class="icon" d="M0 14v8M10 14v8M-8 24h26"/>
    <circle class="icon" cx="5" cy="-8" r="6"/>
    <path class="icon" d="M-6 12a11 9 0 0 1 22 0"/>
    <path class="icon" d="M-34 -28h18v12h-12l-6 5z"/>
  </g>
  <text class="outer-label" x="1355" y="1028">Professional</text>
  <text class="outer-label" x="1355" y="1053">Services &amp;</text>
  <text class="outer-label" x="1355" y="1078">Consulting</text>

  <g class="service service--networking" transform="translate(852,1370)">
    <rect class="icon-backing" x="-44" y="-36" width="88" height="74"/>
    <circle class="icon" cx="4" cy="-14" r="7"/>
    <path class="icon" d="M4 -21v-9M4 -7v6M11 -14h9M-3 -14h-9M9 -19l7 -7M-1 -19l-7 -7M9 -9l7 7M-1 -9l-7 7"/>
    <path class="icon" d="M-32 22l14 -10h18a4 4 0 0 1 0 8h-10M-26 30l12 -8h16l22 -12a4 4 0 0 1 4 7l-24 15h-20l-6 4"/>
  </g>
  <text class="outer-label mid" x="852" y="1428">Networking Services</text>

  <g class="service service--procurement" transform="translate(390,995)">
    <rect class="icon-backing" x="-36" y="-36" width="72" height="72"/>
    <path class="icon" d="M-24 -26h40v44M-24 -26v48h26"/>
    <path class="icon" d="M-10 -20h14v10h-14zM-18 -2l3 3 5 -5M-6 -1h16M-18 8l3 3 5 -5M-6 9h12M-18 18l3 3 5 -5"/>
    <circle class="icon" cx="16" cy="22" r="9"/>
    <path class="icon" d="M16 17v10"/>
  </g>
  <text class="outer-label end" x="352" y="990">Procurement</text>
  <text class="outer-label end" x="352" y="1015">&amp; Licensing</text>

  <g class="service service--telephony" transform="translate(458,615)">
    <rect class="icon-backing" x="-38" y="-36" width="76" height="72"/>
    <rect class="icon" x="-18" y="-26" width="44" height="52" rx="4"/>
    <path class="icon" d="M-22 -22h-6a4 4 0 0 0 -4 4v40a4 4 0 0 0 4 4h6"/>
    <rect class="icon" x="-10" y="-20" width="28" height="9"/>
    <path class="icon" d="M-10 -4h6v5h-6zM1 -4h6v5h-6zM12 -4h6v5h-6zM-10 8h6v5h-6zM1 8h6v5h-6zM12 8h6v5h-6z"/>
  </g>
  <text class="outer-label end" x="420" y="595">Telephony</text>
  <text class="outer-label end" x="420" y="619">&amp; UC</text>

  <!-- Primary services (inner ring) -->
  <g class="service service--software" transform="translate(845,633)">
    <rect class="icon-backing" x="-42" y="-36" width="84" height="72"/>
    <rect class="icon" x="-26" y="-14" width="44" height="30" rx="3"/>
    <path class="icon" d="M-4 16v6M-12 24h16"/>
    <path class="icon" d="M-14 -6v-24h18l8 8v22"/>
    <path class="icon" d="M-9 -24h10M-9 -18h14M-9 -12h14"/>
    <circle class="icon" cx="24" cy="16" r="8"/>
    <circle class="icon" cx="24" cy="16" r="3"/>
  </g>
  <text class="inner-label mid" x="846" y="688">Software</text>

  <g class="service service--managed-it" transform="translate(1072,770)">
    <rect class="icon-backing" x="-38" y="-36" width="76" height="72"/>
    <path class="icon" d="M-12 -28h26l8 8v32h-34z"/>
    <path class="icon" d="M-4 -28v-2M-4 -16h18M-2 -8h16M2 0h12"/>
    <circle class="icon" cx="-12" cy="14" r="12"/>
    <circle class="icon" cx="-12" cy="14" r="4"/>
  </g>
  <text class="inner-label mid" x="1030" y="830">Managed IT</text>

  <g class="service service--draas" transform="translate(1078,1033)">
    <rect class="icon-backing" x="-34" y="-40" width="68" height="80"/>
    <path class="icon" d="M-24 -22h34l8 8v38h-42z"/>
    <path class="icon" d="M-18 -8h6v6h-6zM-18 4h6v6h-6zM-18 16h6v5h-6zM-6 -5h14M-6 7h14"/>
    <path class="icon" d="M-8 -26c0 -6 4 -8 6 -12c2 4 6 6 6 12a6 6 0 0 1 -12 0z"/>
    <circle class="icon" cx="18" cy="22" r="8"/>
  </g>
  <text class="inner-label end" x="1035" y="1050">DRaaS</text>

  <g class="service service--cloud" transform="translate(845,1167)">
    <rect class="icon-backing" x="-44" y="-36" width="88" height="72"/>
    <path class="icon" d="M-22 4a12 12 0 0 1 2 -24a16 16 0 0 1 30 -4a12 12 0 0 1 14 20"/>
    <rect class="icon" x="-20" y="-2" width="42" height="30" rx="2"/>
    <path class="icon" d="M-20 6h42M-6 13l-5 5 5 5M8 13l5 5 -5 5M3 12l-4 12"/>
  </g>
  <text class="inner-label mid" x="850" y="1120">Cloud Services</text>

  <g class="service service--e8" transform="translate(617,1033)">
    <rect class="icon-backing" x="-36" y="-36" width="72" height="72"/>
    <path class="icon" d="M-4 -28l26 9v16c0 16 -11 26 -26 32c-15 -6 -26 -16 -26 -32v-16z"/>
    <circle class="icon" cx="-6" cy="-6" r="5"/>
    <path class="icon" d="M-6 -1v10"/>
    <circle class="icon" cx="18" cy="16" r="11"/>
    <path class="icon" d="M13 16l4 4 6 -7"/>
  </g>
  <text class="inner-label" x="672" y="1026">E8</text>
  <text class="inner-label" x="672" y="1049">Security</text>

  <g class="service service--desktop" transform="translate(616,765)">
    <rect class="icon-backing" x="-38" y="-38" width="76" height="76"/>
    <rect class="icon" x="-30" y="-26" width="60" height="42" rx="6"/>
    <path class="icon" d="M-30 6h60M-6 16v8M6 16v8M-14 26h28"/>
    <path class="icon" d="M0 -20l8 4.5v9l-8 4.5l-8 -4.5v-9z"/>
    <path class="icon" d="M-22 0h4M-12 0h30M-22 -6h4M-12 -6h8"/>
  </g>
  <text class="inner-label" x="607" y="821">Desktop</text>
  <text class="inner-label" x="607" y="846">&amp; Website</text>
</svg>
</body>
</html>
```